Business cards

Design business cards for our company. Just a straight, business like design with the logo, name, function and contact details

Target Market(s)

We are a innovative technological company active in water treatment

Industry/Entity Type

Water management

Contact Information for Business Card

Name, Function, email, telephone number, link to website

```html
<!DOCTYPE html>
<html lang="en">
<head>
<meta charset="utf-8">
<title>Orcavia Business Cards</title>
<link rel="stylesheet" href="https://fonts.googleapis.com/css2?family=Lato:wght@400;700&family=Montserrat:wght@400;700&display=swap">
<style>
  :root {
    --bg: #2b2d30;
    --card-white: #ffffff;
    --card-dark: #3b3b3c;
    --brand-blue: #2a9ad6;
    --text-grey: #6f7174;
    --faint: #eeeff1;
  }
  * { margin: 0; padding: 0; box-sizing: border-box; }
  html, body { width: 1200px; height: 952px; overflow: hidden; }
  body {
    background: var(--bg);
    font-family: "Lato", sans-serif;
    position: relative;
  }
  .card {
    position: absolute;
    width: 560px;
    height: 320px;
    border-radius: 24px;
    overflow: hidden;
    box-shadow: 0 18px 40px rgba(0,0,0,0.45);
  }
  .card-front { left: 580px; top: 150px; background: var(--card-white); }
  .card-back  { left: 60px;  top: 480px; background: var(--card-dark); }

  .brand {
    display: flex; align-items: center; gap: 10px;
    font-family: "Lato", sans-serif; font-weight: 400;
    color: var(--brand-blue);
  }
  .brand-dot { border-radius: 50%; background: var(--brand-blue); }
  .card-front .brand { position: absolute; left: 44px; top: 36px; font-size: 34px; }
  .card-front .brand-dot { width: 22px; height: 22px; }

  .contact-band { position: absolute; left: 0; top: 0; width: 560px; height: 320px; }
  .contact-list {
    position: absolute; left: 30px; top: 132px;
    list-style: none; color: #fff; font-size: 13px; line-height: 1.3;
  }
  .contact-list li { display: flex; align-items: flex-start; gap: 10px; margin-bottom: 8px; }
  .contact-list li:first-child { color: var(--text-grey); margin-bottom: 12px; }
  .icon {
    flex: none; width: 16px; height: 16px; border-radius: 3px;
    background: #fff; display: flex; align-items: center; justify-content: center;
  }
  .contact-list li:first-child .icon { background: var(--brand-blue); }

  .person { position: absolute; right: 38px; top: 118px; text-align: right; }
  .person-name {
    font-family: "Montserrat", sans-serif; font-size: 22px;
    color: var(--brand-blue); letter-spacing: 0.5px;
  }
  .person-name strong { font-weight: 700; }
  .person-role { font-size: 16px; color: var(--text-grey); margin-top: 4px; letter-spacing: 0.5px; }

  .faint-mark {
    position: absolute; right: 60px; bottom: -40px;
    width: 190px; height: 190px; border-radius: 50%; background: var(--faint);
  }

  .card-back .brand {
    position: absolute; left: 0; right: 0; top: 0; bottom: 0;
    justify-content: center; font-size: 54px;
  }
  .card-back .brand-dot { width: 34px; height: 34px; }
</style>
</head>
<body>

<section class="card card-front" aria-label="Business card front">
  <div class="faint-mark"></div>
  <svg class="contact-band" viewBox="0 0 560 320" aria-hidden="true">
    <path d="M0 118 H268 L252 320 H0 Z" fill="#2a9ad6"/>
    <path d="M0 118 H160 V130 H0 Z" fill="#ffffff"/>
  </svg>

  <div class="brand"><span class="brand-dot"></span><span class="brand-name">Orcavia</span></div>

  <ul class="contact-list">
    <li>
      <span class="icon"><svg width="10" height="10" viewBox="0 0 10 10"><path d="M5 0.5a3.2 3.2 0 0 0-3.2 3.2C1.8 6.2 5 9.5 5 9.5s3.2-3.3 3.2-5.8A3.2 3.2 0 0 0 5 .5z" fill="#fff"/><circle cx="5" cy="3.7" r="1.2" fill="#2a9ad6"/></svg></span>
      <span>1520 Harbor Lane<br>Portland, OR 97201</span>
    </li>
    <li>
      <span class="icon"><svg width="10" height="10" viewBox="0 0 10 10"><path d="M2 0.8l1.6 2-1 1.1a6 6 0 0 0 3.5 3.5l1.1-1 2 1.6-.9 1.5C4.5 9.3.7 5.5.5 1.7z" fill="#2a9ad6"/></svg></span>
      <span>+00 987 654 32</span>
    </li>
    <li>
      <span class="icon"><svg width="10" height="8" viewBox="0 0 10 8"><rect x="0.5" y="0.5" width="9" height="7" fill="none" stroke="#2a9ad6"/><path d="M0.5 0.5 5 4.5 9.5 0.5" fill="none" stroke="#2a9ad6"/></svg></span>
      <span>hello@orcavia.com</span>
    </li>
    <li>
      <span class="icon"><svg width="10" height="10" viewBox="0 0 10 10"><path d="M2 1 8 5 5.2 5.6 6.8 8.6 5.6 9.2 4 6.2 2 8z" fill="#2a9ad6"/></svg></span>
      <span>www.orcavia.com</span>
    </li>
  </ul>

  <div class="person">
    <p class="person-name">DANIEL M. <strong>HARTLEY</strong></p>
    <p class="person-role">Managing Director</p>
  </div>
</section>

<section class="card card-back" aria-label="Business card back">
  <div class="brand"><span class="brand-dot"></span><span class="brand-name">Orcavia</span></div>
</section>

</body>
</html>
```